Tallowick Limited Business Card

We need a business card for a new company based in Essex, United Kingdom. We develop and manufacture educational games. The business card needs to match the company brand and logo and the colour scheme.
My company makes educational board games to be played by the family or used by teachers
The games are tile based number game

Target Market(s)

Parents, teachers, schools and children

Industry/Entity Type

Games

Contact Information for Business Card

Company Name - Tallowick Limited
Director - Damian Prouse
Registered Office - 3 Marsh Court, 142 Quarry Lane, Brindleford, Essex, CM7 4XR
Phone Number - 07950 000 318
Email - Enquiries@Tallowick.example
Website - www.Tallowick.example
Company Number - 00000000

Font styles to use
Sans Serif

Colors
00a990
ffffff

Requirements
Must have
• Same colour scheme as the attachments - green and white
• Same font style for Tallowick
• Images of the number tiles similar to the attachments
• extra details
• The colour is Cyan - 82 Magenta - 24 Yellow - 44 Black - 2
• I have attached some of the font styles use on my website and alos my LOGO
Nice to have
• Image of the number "1" tag as seen on the website

```html
<!DOCTYPE html>
<html lang="en">
<head>
<meta charset="utf-8">
<title>Tallowick Limited – Stationery</title>
<link rel="stylesheet" href="https://fonts.googleapis.com/css2?family=Montserrat:wght@400;500;600;700&family=Arimo:wght@400;700&display=swap">
<style>
  :root{
    --teal:#12898a;
    --teal-dark:#0e7778;
    --paper:#f1f1f1;
    --paper-shade:#e3e3e3;
    --ink:#3a3a3a;
    --ink-soft:#8a8a8a;
    --rule:#9a9a9a;
    --stage:#dcdcdc;
    --white:#ffffff;
  }
  *{box-sizing:border-box;margin:0;padding:0}
  html,body{width:1200px;height:932px;overflow:hidden}
  body{background:var(--stage);font-family:"Montserrat",sans-serif;color:var(--ink);position:relative}
  .sprite{position:absolute;width:0;height:0;overflow:hidden}

  .sheet{position:absolute;background:var(--paper);overflow:hidden;box-shadow:0 6px 14px rgba(0,0,0,.12)}
  .brand-name{font-family:"Montserrat",sans-serif;font-weight:600;color:var(--teal);line-height:1;letter-spacing:-.5px;display:block}
  .brand-tag{font-family:"Montserrat",sans-serif;font-weight:400;color:var(--teal);text-transform:uppercase;line-height:1;display:block}
  .caps{text-transform:uppercase;letter-spacing:.6px;color:#555}
  .contact-list{list-style:none}
  .contact-list li{display:flex;align-items:center;gap:4px}
  .icon{width:1em;height:1em;fill:var(--teal);flex:none}
  .product-shot{position:absolute;background:radial-gradient(ellipse at 45% 50%,#2aa5a4 0%,#16908f 55%,rgba(20,140,140,0) 72%)}
  .number-strip{position:absolute;right:0;bottom:0;background:var(--teal);color:var(--white);font-weight:600;text-transform:uppercase;letter-spacing:.5px;display:flex;align-items:center;justify-content:flex-end;clip-path:polygon(7% 0,100% 0,100% 100%,0 100%)}
  .base-rule{position:absolute;left:0;bottom:0;background:var(--rule)}

  /* Letterhead */
  .letterhead{left:40px;top:98px;width:520px;height:735px}
  .letterhead .brand{position:absolute;left:30px;top:30px}
  .letterhead .brand-name{font-size:37px}
  .letterhead .brand-tag{font-size:12.5px;margin-top:5px;letter-spacing:.3px}
  .letterhead .address{position:absolute;right:170px;top:34px;text-align:right;font-size:6.8px;line-height:11px}
  .letterhead .divider{position:absolute;left:358px;top:32px;width:1.5px;height:34px;background:var(--teal)}
  .letterhead .contact-list{position:absolute;left:366px;top:34px;font-size:6.8px;line-height:11px}
  .meta{position:absolute;top:204px;font-family:"Arimo",sans-serif}
  .meta dt{font-size:9px;font-weight:700;color:#222}
  .meta dd{font-size:8px;color:var(--ink-soft);margin-top:3px}
  .meta-subject{left:158px}
  .meta-date{left:434px}
  .letter-body{position:absolute;left:158px;top:270px;width:322px;font-family:"Arimo",sans-serif}
  .salutation{font-size:11px;color:#444;margin-bottom:12px}
  .letter-body p{font-size:7.9px;line-height:11.3px;color:var(--ink-soft);text-align:justify;margin-bottom:11px}
  .sidebar-note{position:absolute;right:392px;top:332px;width:110px;text-align:right;font-family:"Arimo",sans-serif;font-size:7.9px;line-height:11.3px}
  .sidebar-note .lead{color:#333}
  .sidebar-note .soft{color:var(--ink-soft)}
  .sidebar-note p+p{margin-top:6px}
  .signature{position:absolute;left:186px;top:600px;font-family:"Arimo",sans-serif;font-size:11px;line-height:14px;color:#555}
  .letterhead .product-shot{left:-10px;top:568px;width:190px;height:170px}
  .letterhead .number-strip{width:200px;height:20px;bottom:3px;font-size:7.5px;padding-right:12px}
  .letterhead .base-rule{width:330px;height:5px}

  /* Business card */
  .card{width:275px;height:158px;top:68px}
  .card-front{left:590px}
  .card-front .brand{position:absolute;left:14px;top:12px}
  .card-front .brand-name{font-size:27px}
  .card-front .brand-tag{font-size:9.2px;margin-top:3px}
  .card-front .person{position:absolute;left:15px;top:68px}
  .person-name{font-size:6.2px;font-weight:700;color:var(--teal);text-transform:uppercase;letter-spacing:.4px}
  .person-role{font-size:4.8px;text-transform:uppercase;color:#666;margin-top:2px;letter-spacing:.4px}
  .card-front .address{position:absolute;left:15px;top:92px;font-size:4.8px;line-height:8px}
  .card-front .contact-list{position:absolute;left:15px;top:118px;font-size:4.8px;line-height:8px}
  .card-front .product-shot{left:150px;top:48px;width:122px;height:96px}
  .card-front .number-strip{width:118px;height:9px;bottom:2px;font-size:4.6px;padding-right:8px}
  .card-front .base-rule{width:170px;height:3px}
  .card-back{left:885px;background:var(--teal);display:flex;flex-direction:column;align-items:center;justify-content:center}
  .card-back .brand-name{font-size:30px;color:var(--white)}
  .card-back .brand-tag{font-size:9.5px;color:var(--white);margin-top:4px;text-align:center}

  /* Compliment slip */
  .slip{left:590px;top:250px;width:570px;height:285px}
  .slip .brand{position:absolute;left:26px;top:22px}
  .slip .brand-name{font-size:37px}
  .slip .brand-tag{font-size:12.5px;margin-top:5px}
  .slip .address{position:absolute;left:22px;top:182px;font-size:7.4px;line-height:11.5px}
  .slip .contact-list{position:absolute;left:22px;top:224px;font-size:7.4px;line-height:11.5px}
  .slip .product-shot{left:360px;top:88px;width:205px;height:160px}
  .slip .number-strip{width:195px;height:17px;bottom:4px;font-size:7.6px;padding-right:16px}
  .slip .base-rule{width:390px;height:5px}

  /* Envelope */
  .envelope{position:absolute;left:590px;top:560px;width:570px;height:303px;background:var(--paper-shade);box-shadow:0 6px 14px rgba(0,0,0,.12)}
  .envelope svg{position:absolute;inset:0}
  .envelope .brand{position:absolute;left:0;top:20px;width:100%;text-align:center}
  .envelope .brand-name{font-size:31px;color:var(--white)}
  .envelope .brand-tag{font-size:10.5px;color:var(--white);margin-top:3px}
</style>
</head>
<body>

<svg class="sprite" aria-hidden="true">
  <symbol id="i-phone" viewBox="0 0 16 16"><path d="M3.6 1.2l2.2 2.4c.4.4.4 1 0 1.4L4.8 6c.9 2 2.6 3.7 4.6 4.6l1-1c.4-.4 1-.4 1.4 0l2.4 2.2c.4.4.4 1 0 1.4l-1.3 1.3C11.6 15.8 8 14.6 5 11.6S.2 4.4 1.5 3.1L2.2 1.2c.4-.4 1-.4 1.4 0z"/></symbol>
  <symbol id="i-mail" viewBox="0 0 16 16"><path d="M1 3h14v10H1zM2.5 4.5v.3L8 8.6l5.5-3.8v-.3zM2.5 6.6v4.9h11V6.6L8 10.4z" fill-rule="evenodd"/></symbol>
  <symbol id="i-web" viewBox="0 0 16 16"><path d="M8 1a7 7 0 100 14A7 7 0 008 1zm5.4 6.2h-2.3a11 11 0 00-1-4.2 5.6 5.6 0 013.3 4.2zM8 2.6c.6.8 1.4 2.4 1.6 4.6H6.4C6.6 5 7.4 3.4 8 2.6zM5.9 3a11 11 0 00-1 4.2H2.6A5.6 5.6 0 015.9 3zM2.6 8.8h2.3a11 11 0 001 4.2 5.6 5.6 0 01-3.3-4.2zM8 13.4c-.6-.8-1.4-2.4-1.6-4.6h3.2c-.2 2.2-1 3.8-1.6 4.6zm2.1-.4a11 11 0 001-4.2h2.3a5.6 5.6 0 01-3.3 4.2z"/></symbol>
</svg>

<!-- Letterhead -->
<article class="sheet letterhead" aria-label="Letterhead">
  <header class="brand">
    <span class="brand-name">Tallowick</span>
    <span class="brand-tag">Fast paced number games</span>
  </header>
  <address class="address caps" style="font-style:normal">
    3 Marsh Court,<br>142 Quarry Lane,<br>Brindleford, Essex, CM7 4XR
  </address>
  <span class="divider"></span>
  <ul class="contact-list caps">
    <li><svg class="icon"><use href="#i-phone"/></svg>07950 000 318</li>
    <li><svg class="icon"><use href="#i-mail"/></svg>Enquiries@Tallowick.example</li>
    <li><svg class="icon"><use href="#i-web"/></svg>www.Tallowick.example</li>
  </ul>

  <dl class="meta meta-subject"><dt>SUBJECT :</dt><dd>Lorem Ipsum is simply dummy</dd></dl>
  <dl class="meta meta-date"><dt>DATE :</dt><dd>15-09-2017</dd></dl>

  <aside class="sidebar-note">
    <p class="lead">Lorem Ipsum is simply dummy text of the printing</p>
    <p><span class="lead">Lorem Ipsum is</span><br><span class="soft">simply dummy text</span></p>
  </aside>

  <section class="letter-body">
    <p class="salutation">Dear Person,</p>
    <p>Lorem Ipsum is simply dummy text of the printing and typesetting industry. Lorem Ipsum has been the industry's standard dummy text ever since the 1500s, when an unknown printer took a galley of type and scrambled it to make a type specimen book. It has survived not only five centuries, but also the leap into electronic typesetting, remaining essentially unchanged. It was popularised in the 1960s with the release of Typeleaf sheets containing Lorem Ipsum passages, and more recently with desktop publishing software like Quillset Composer including versions of Lorem Ipsum.</p>
    <p>Lorem Ipsum is simply dummy text of the printing and typesetting industry. Lorem Ipsum has been the industry's standard dummy text ever since the 1500s, when an unknown printer took a galley of type and scrambled it to make a type specimen book. It has survived not only five centuries, but also the leap into electronic typesetting, remaining essentially unchanged. It was popularised in the 1960s with the release.</p>
    <p>Typeleaf sheets containing Lorem Ipsum passages, and more recently with desktop publishing software like Quillset Composer including versions of Lorem Ipsum. Typeleaf sheets containing Lorem Ipsum passages, and more recently with desktop publishing software like Quillset Composer including versions of Lorem Ipsum.</p>
  </section>

  <p class="signature">Penworthy<br>Managing Director</p>

  <div class="product-shot" role="img" aria-label="Product photo: zipped teal game case printed with number tiles, with a swing tag"></div>
  <div class="number-strip">Company Number - 00000000</div>
  <div class="base-rule"></div>
</article>

<!-- Business card front -->
<article class="sheet card card-front" aria-label="Business card front">
  <header class="brand">
    <span class="brand-name">Tallowick</span>
    <span class="brand-tag">Fast paced number games</span>
  </header>
  <div class="person">
    <p class="person-name">Damian Prouse</p>
    <p class="person-role">Director</p>
  </div>
  <address class="address caps" style="font-style:normal">
    3 Marsh Court,<br>142 Quarry Lane,<br>Brindleford, Essex, CM7 4XR
  </address>
  <ul class="contact-list caps">
    <li><svg class="icon"><use href="#i-phone"/></svg>07950 000 318</li>
    <li><svg class="icon"><use href="#i-mail"/></svg>Enquiries@Tallowick.example</li>
    <li><svg class="icon"><use href="#i-web"/></svg>www.Tallowick.example</li>
  </ul>
  <div class="product-shot" role="img" aria-label="Product photo: zipped teal game case printed with number tiles, with a swing tag"></div>
  <div class="number-strip">Company Number - 00000000</div>
  <div class="base-rule"></div>
</article>

<!-- Business card back -->
<article class="sheet card card-back" aria-label="Business card back">
  <span class="brand-name">Tallowick</span>
  <span class="brand-tag">Fast paced number games</span>
</article>

<!-- Compliment slip -->
<article class="sheet slip" aria-label="Compliment slip">
  <header class="brand">
    <span class="brand-name">Tallowick</span>
    <span class="brand-tag">Fast paced number games</span>
  </header>
  <address class="address caps" style="font-style:normal">
    3 Marsh Court,<br>142 Quarry Lane,<br>Brindleford, Essex, CM7 4XR
  </address>
  <ul class="contact-list caps">
    <li><svg class="icon"><use href="#i-phone"/></svg>07950 000 318</li>
    <li><svg class="icon"><use href="#i-mail"/></svg>Enquiries@Tallowick.example</li>
    <li><svg class="icon"><use href="#i-web"/></svg>www.Tallowick.example</li>
  </ul>
  <div class="product-shot" role="img" aria-label="Product photo: zipped teal game case printed with number tiles, with a swing tag"></div>
  <div class="number-strip">Company Number - 00000000</div>
  <div class="base-rule"></div>
</article>

<!-- Envelope -->
<article class="envelope" aria-label="Envelope back">
  <svg width="570" height="303" viewBox="0 0 570 303" aria-hidden="true">
    <path d="M6 60 L6 296 L564 296 L564 60" fill="none" stroke="#cfcfcf" stroke-width="1"/>
    <path d="M6 296 L250 170 Q285 152 320 170 L564 296" fill="none" stroke="#d2d2d2" stroke-width="1"/>
    <path d="M0 0 H570 V40 Q558 58 520 64 L306 96 Q285 99 264 96 L50 64 Q12 58 0 40 Z" fill="#12898a"/>
  </svg>
  <header class="brand">
    <span class="brand-name">Tallowick</span>
    <span class="brand-tag">Fast paced number games</span>
  </header>
</article>

</body>
</html>
```